Dietitian needs awesome business card

I need a contemporary design that's eye catching but professional.
My card is to given to doctors, specialists and patients alike.
I manage patients with chronic diseases
I have uploaded my logo and current business card, I would also like the other Registered Clinical Nutritionist logo incorporated into the design

Target Market(s)

Doctors, specialists and patients

Industry/Entity Type

Healthcare

Contact Information for Business Card

www.brindlecovenutrition.com.au
Ph: 0427 516 903
Fax: 6482 7315
email: marcus.k.wellfare@quorvamail.com
Space on the back of the card with: Appointment date, Appointment time and appointment location

Font styles to use
Serif

Colors
fbee3e
876aae
ffc214

Requirements
Must have
• My Logo
• Registered Clinical Nutritionist Logo
• My 4 locations - Fernhollow Medical Centre, North Kelby Health, Ashcourt Medical, Pinebrook Doctors Surgery
Nice to have
• I like the colours in my current business card

```html
<!DOCTYPE html>
<html lang="en">
<head>
<meta charset="utf-8">
<title>Brindle Cove Nutrition &amp; Dietetics – Business Card</title>
<link href="https://fonts.googleapis.com/css2?family=Montserrat:wght@400;500;600&family=Libre+Baskerville:wght@400&display=swap" rel="stylesheet">
<style>
  :root {
    --navy: #243b8f;
    --blue: #1f3f94;
    --green: #3fae49;
    --lime: #b5d433;
    --orange: #f47a20;
    --paper: #ffffff;
    --stage: #e6e7ea;
    --ink: #26357f;
  }
  * { margin: 0; padding: 0; box-sizing: border-box; }
  html, body { width: 1200px; height: 900px; overflow: hidden; }
  body { background: var(--stage); position: relative; font-family: "Montserrat", sans-serif; }

  .card {
    position: absolute;
    width: 560px; height: 320px;
    background: var(--paper);
    border-radius: 22px;
    overflow: hidden;
    box-shadow: 0 10px 30px rgba(0,0,0,.18);
  }
  .card--back { left: 90px; top: 90px; }
  .card--front { left: 550px; top: 490px; }

  .brand { position: absolute; display: flex; align-items: center; gap: 12px; }
  .brand__dot { width: 48px; height: 48px; border-radius: 50%; background: var(--blue); flex: none; }
  .brand__name { font-weight: 500; font-size: 22px; line-height: 1.1; color: var(--blue); }

  /* appointment side */
  .card--back .brand { left: 150px; top: 36px; }
  .credentials {
    position: absolute; left: 0; right: 0; top: 112px; text-align: center;
    font-family: "Libre Baskerville", serif; font-size: 15px; color: var(--ink);
  }
  .appointment__title {
    position: absolute; left: 0; right: 0; top: 146px; text-align: center;
    font-weight: 600; font-size: 20px; color: var(--green);
  }
  .field { position: absolute; display: flex; align-items: flex-end; font-size: 16px; color: var(--ink); }
  .field__line { flex: 1; border-bottom: 1.5px solid var(--ink); margin-left: 6px; height: 18px; }
  .field--date { left: 40px; top: 208px; width: 270px; }
  .field--time { left: 320px; top: 208px; width: 200px; }
  .field--location { left: 40px; top: 260px; width: 480px; }

  /* contact side */
  .card--front .brand { left: 36px; top: 40px; }
  .holder {
    position: absolute; right: 40px; top: 96px;
    font-family: "Libre Baskerville", serif; font-size: 22px; color: var(--navy);
  }
  .holder__surname { color: var(--green); }
  .rule { position: absolute; height: 1.5px; background: var(--navy); }
  .rule--name { left: 250px; right: 30px; top: 132px; }
  .rule--contact { left: 30px; width: 320px; top: 214px; }
  .cred-badge {
    position: absolute; right: 40px; top: 142px; width: 120px; height: 56px;
    background: var(--orange); display: flex; align-items: center; justify-content: flex-end; padding-right: 12px;
  }
  .cred-badge__mark { width: 34px; height: 34px; border-radius: 50%; border: 2px solid #fff; }
  .contacts { position: absolute; left: 36px; top: 224px; list-style: none; }
  .contacts li { display: flex; align-items: center; gap: 12px; font-size: 15px; color: var(--ink); line-height: 19px; }
  .contacts svg { width: 12px; height: 12px; flex: none; }
  .band { position: absolute; inset: 0; }
</style>
</head>
<body>

<section class="card card--back" aria-label="Appointment side">
  <div class="brand">
    <span class="brand__dot"></span>
    <span class="brand__name">Brindle Cove<br>Nutrition &amp; Dietetics</span>
  </div>
  <p class="credentials">Registered Clinical Nutritionist, Nutrionist and Chef</p>
  <p class="appointment__title">Appointment:</p>
  <div class="field field--date">Date:<span class="field__line"></span></div>
  <div class="field field--time">Time:<span class="field__line"></span></div>
  <div class="field field--location">Location:<span class="field__line"></span></div>
</section>

<section class="card card--front" aria-label="Contact side">
  <svg class="band" viewBox="0 0 560 320" preserveAspectRatio="none" aria-hidden="true">
    <polygon points="446,204 560,204 560,320 426,320" fill="var(--navy)"/>
    <polygon points="0,310 428,304 426,320 0,320" fill="var(--lime)"/>
  </svg>
  <div class="brand">
    <span class="brand__dot"></span>
    <span class="brand__name">Brindle Cove<br>Nutrition &amp; Dietetics</span>
  </div>
  <p class="holder">Marcus <span class="holder__surname">Kellaway</span></p>
  <span class="rule rule--name"></span>
  <div class="cred-badge" aria-label="Credential badge"><span class="cred-badge__mark"></span></div>
  <span class="rule rule--contact"></span>
  <ul class="contacts">
    <li><svg viewBox="0 0 12 12"><path d="M2 1l2.5 0 1 3-1.5 1a7 7 0 0 0 3 3l1-1.5 3 1V11C5 11 1 7 1 2z" fill="var(--green)"/></svg>0427 516 903</li>
    <li><svg viewBox="0 0 12 12"><rect x="1" y="4" width="10" height="6" rx="1" fill="var(--green)"/><rect x="3" y="1" width="6" height="3" fill="var(--green)"/></svg>6482 7315</li>
    <li><svg viewBox="0 0 12 12"><rect x="1" y="2.5" width="10" height="7" fill="none" stroke="var(--green)" stroke-width="1.3"/><path d="M1 3l5 4 5-4" fill="none" stroke="var(--green)" stroke-width="1.3"/></svg>marcus.k.wellfare@quorvamail.com</li>
    <li><svg viewBox="0 0 12 12"><circle cx="6" cy="6" r="5" fill="none" stroke="var(--green)" stroke-width="1.2"/><ellipse cx="6" cy="6" rx="2.2" ry="5" fill="none" stroke="var(--green)" stroke-width="1"/><path d="M1 6h10" stroke="var(--green)" stroke-width="1"/></svg>www.brindlecovenutrition.com.au</li>
  </ul>
</section>

</body>
</html>
```